Business card for femtech company

Nothing too elaborate but elegant and geared towards the mother and baby market. Prefer full-bleed with logo (attached) rear.

```html
<!DOCTYPE html>
<html lang="en">
<head>
<meta charset="utf-8">
<title>Nurelia — Business Card</title>
<link rel="stylesheet" href="https://fonts.googleapis.com/css2?family=Lato:wght@400;700&display=swap">
<style>
  :root {
    --page-bg: #2b2d30;
    --card-white: #ffffff;
    --card-grey: #a9a9aa;
    --teal: #4fc1b2;
    --ink-grey: #8d8d8f;
    --text-grey: #7a7a7c;
    --faint-mark: #f1f1f3;
    --faint-mark-back: #b6b6b8;
    --white: #ffffff;
  }
  * { box-sizing: border-box; margin: 0; padding: 0; }
  html, body {
    width: 1200px; height: 952px; overflow: hidden;
    background: var(--page-bg);
    font-family: "Lato", sans-serif;
  }
  .canvas {
    position: relative; width: 1200px; height: 952px;
  }
  .card {
    position: absolute; left: 270px; width: 660px; height: 377px;
    overflow: hidden; border-radius: 2px;
    box-shadow: 0 10px 30px rgba(0,0,0,.45);
  }
  .card--front { top: 64px; background: var(--card-white); }
  .card--back { top: 511px; background: var(--card-grey); }

  /* front */
  .front__brand {
    position: absolute; left: 44px; top: 40px;
    display: flex; align-items: center; gap: 18px;
  }
  .brand__dot {
    width: 62px; height: 62px; border-radius: 50%;
    background: var(--teal);
  }
  .brand__name {
    font-size: 54px; font-weight: 400; color: var(--ink-grey);
    letter-spacing: 1px; line-height: 1;
  }
  .front__person {
    position: absolute; left: 44px; top: 138px;
  }
  .person__name {
    font-size: 17px; font-weight: 700; color: var(--teal);
    letter-spacing: 1px; text-transform: uppercase;
  }
  .person__role {
    font-size: 13px; color: var(--text-grey); margin-top: 4px;
  }
  .contact-list {
    list-style: none; margin-top: 16px;
  }
  .contact-list li {
    display: flex; align-items: center; gap: 10px;
    font-size: 12px; color: var(--text-grey); margin-bottom: 8px;
  }
  .contact-icon {
    width: 16px; height: 16px; border-radius: 3px; background: var(--teal);
    display: flex; align-items: center; justify-content: center;
  }
  .front__rule {
    position: absolute; left: 0; bottom: 40px;
    width: 300px; height: 4px; background: var(--teal);
  }
  .front__decor {
    position: absolute; right: 150px; bottom: -150px;
    width: 300px; height: 300px; border-radius: 50%;
    background: var(--faint-mark);
  }

  /* back */
  .back__decor {
    position: absolute; left: -60px; top: -120px;
    width: 340px; height: 340px; border-radius: 50%;
    background: var(--faint-mark-back);
  }
  .back__name {
    position: absolute; right: 60px; bottom: 56px;
    font-size: 72px; font-weight: 400; color: var(--white);
    letter-spacing: 2px; line-height: 1;
  }
</style>
</head>
<body>
<main class="canvas">
  <section class="card card--front" aria-label="Card front">
    <div class="front__decor" aria-hidden="true"></div>
    <div class="front__brand">
      <span class="brand__dot" aria-hidden="true"></span>
      <span class="brand__name">Nurelia</span>
    </div>
    <div class="front__person">
      <p class="person__name">Daniel R. Hartley</p>
      <p class="person__role">Managing Director</p>
      <ul class="contact-list">
        <li>
          <span class="contact-icon">
            <svg width="10" height="10" viewBox="0 0 10 10"><path d="M2 1 L4 1 L4.6 3 L3.4 3.8 Q4.4 5.8 6.2 6.6 L7 5.4 L9 6 L9 8 Q5 9 1.6 5 Q0.8 3 2 1 Z" fill="#fff"/></svg>
          </span>
          +00 987 654 32
        </li>
        <li>
          <span class="contact-icon">
            <svg width="10" height="8" viewBox="0 0 10 8"><rect x="0.5" y="0.5" width="9" height="7" fill="none" stroke="#fff"/><path d="M0.5 0.5 L5 4.5 L9.5 0.5" fill="none" stroke="#fff"/></svg>
          </span>
          hello@nurelia.com
        </li>
        <li>
          <span class="contact-icon">
            <svg width="10" height="10" viewBox="0 0 10 10"><circle cx="5" cy="5" r="4" fill="none" stroke="#fff"/><path d="M1 5 H9 M5 1 Q2.5 5 5 9 M5 1 Q7.5 5 5 9" fill="none" stroke="#fff" stroke-width=".8"/></svg>
          </span>
          www.nurelia.com
        </li>
      </ul>
    </div>
    <div class="front__rule" aria-hidden="true"></div>
  </section>

  <section class="card card--back" aria-label="Card back">
    <div class="back__decor" aria-hidden="true"></div>
    <p class="back__name">Nurelia</p>
  </section>
</main>
</body>
</html>
```